Fastest Work at home Solution for Small Businesses

We need a web page for a product called *CopperVale*
We develop an innovative VPN Appliance (Model-Name ->Vale Nine) that gives small business the possibility literally setup the possibility for Companies to let their employees work from home.
With our secure appliance we create safe connection between any business and the employee *working at home*
Our Products *Vale Nine* are rolled out in minutes.
A. Employees can connect directly
B. Work from any location
C. All this without having to change the company firewall
Use case
=======
1. Go to our page
2. Select Product
3. Order
4. Connect to any Switch in the company
5. install software on employees laptop
***** INSTANT Connection ******
Businesses

```html
<!DOCTYPE html>
<html lang="en">
<head>
<meta charset="utf-8">
<title>CopperVale – Work From Home VPN Appliance</title>
<link href="https://fonts.googleapis.com/css2?family=Rubik:wght@400;500;700&family=Lora:ital@1&display=swap" rel="stylesheet">
<style>
:root{
  --navy:#0a2a63;
  --deep:#062257;
  --blue:#0d56c9;
  --bright:#1a72e0;
  --sky:#dce8f7;
  --page:#f6f8fc;
  --ink:#1b2437;
  --muted:#6d7688;
  --white:#ffffff;
  --accent:#f06a35;
}
*{margin:0;padding:0;box-sizing:border-box}
html,body{width:1200px;height:3393px;overflow:hidden}
body{position:relative;background:var(--page);font-family:"Rubik",sans-serif;color:var(--ink)}
.abs{position:absolute}
.center{left:0;width:1200px;text-align:center}

/* hero */
.hero-bg{left:0;top:0;width:1200px;height:700px}
.nav{top:26px;left:92px;width:1016px;height:40px;display:flex;align-items:center}
.brand{display:flex;align-items:center;gap:10px;color:var(--white);font-size:38px;font-weight:500}
.brand-mark{width:30px;height:30px;background:var(--bright);border-radius:4px}
.nav-links{margin-left:auto;display:flex;gap:44px;align-items:center;list-style:none}
.nav-links li{color:var(--white);font-size:12.5px;font-weight:500;letter-spacing:.3px}
.nav-links .login{border:2px solid var(--bright);border-radius:6px;padding:10px 28px}
.hero-title{top:232px;color:var(--white);font-size:47px;font-weight:700;line-height:53px;letter-spacing:.5px}
.hero-text{top:350px;left:355px;width:490px;text-align:center;color:var(--white);font-size:11px;line-height:17px;letter-spacing:.3px}
.btn{top:428px;left:514px;width:171px;height:55px;background:var(--blue);color:var(--white);border-radius:4px;display:flex;align-items:center;justify-content:center;font-size:13.5px;letter-spacing:1px;box-shadow:0 6px 18px rgba(0,0,0,.25)}

.eyebrow{font-size:9.5px;letter-spacing:1px;color:var(--muted);text-transform:uppercase}
.section-title{font-size:29px;font-weight:700;color:var(--navy)}
.rule{left:548px;width:104px;height:3px;background:var(--blue)}

/* products */
.card{width:249px;height:342px;background:#f4f4f5;box-shadow:0 4px 14px rgba(20,40,90,.12);border-radius:3px;overflow:hidden}
.card-art{height:226px;background:linear-gradient(160deg,#ffffff,#dfe7f4)}
.card h3{margin-top:27px;text-align:center;font-size:11.2px;font-weight:500;color:var(--ink)}
.card p{margin:12px auto 0;width:170px;text-align:center;font-size:9.2px;line-height:15px;color:var(--muted)}

/* steps */
.step{width:205px;height:230px;background:var(--white);box-shadow:0 2px 10px rgba(20,40,90,.1)}
.step .num{position:absolute;top:-11px;left:89px;width:22px;height:22px;border-radius:50%;background:var(--blue);color:var(--white);font-size:10px;font-weight:700;display:flex;align-items:center;justify-content:center}
.step svg{display:block;margin:40px auto 0}
.step h3{margin-top:16px;text-align:center;font-size:11px;font-weight:500}
.step p{margin:12px auto 0;width:150px;text-align:center;font-size:9.3px;line-height:15px;color:var(--muted)}
.dash{height:0;border-top:1px dashed #b6bfcc}

/* testimonials */
.quote{top:2398px;left:300px;width:600px;text-align:center;font-family:"Lora",serif;font-style:italic;font-size:16.5px;line-height:26px;color:var(--muted)}
.arrow{top:2410px}

/* partners */
.partners{top:2822px;left:240px;width:720px;display:flex;justify-content:space-between;align-items:center}
.badge{width:90px;height:58px;border-radius:8px;background:#c9d2df}

/* footer */
.footer-bg{left:0;top:2910px;width:1200px;height:483px}
.foot{color:var(--white);font-size:10px;line-height:17px}
.foot h4{font-size:11px;font-weight:500;color:#3d8df5;margin-bottom:8px}
.foot-rule{width:88px;height:2px;background:var(--bright)}
.foot-links{list-style:none}
.foot-links li{font-size:10px;height:26px;font-weight:500}
.foot-links li::before{content:"›";color:#3d8df5;margin-right:8px}
.contact-row{display:flex;gap:16px;align-items:flex-start;font-size:10px;line-height:17px}
.social{width:20px;height:20px;border-radius:50%;background:var(--white)}
</style>
</head>
<body>

<svg class="abs hero-bg" viewBox="0 0 1200 700" aria-hidden="false" role="img" aria-label="Blue hero backdrop with a glowing globe and circuit lines">
  <defs>
    <radialGradient id="heroGlow" cx="0.5" cy="0.38" r="0.65">
      <stop offset="0" stop-color="#2f7fd8"/>
      <stop offset="0.55" stop-color="#0d4fa8"/>
      <stop offset="1" stop-color="#0a2f73"/>
    </radialGradient>
  </defs>
  <path d="M0 0H1200V690C1060 700 930 640 800 590C650 530 470 520 350 540C210 565 100 660 0 650Z" fill="url(#heroGlow)"/>
</svg>

<nav class="abs nav">
  <div class="brand"><span class="brand-mark"></span>CopperVale</div>
  <ul class="nav-links">
    <li>HOME</li><li>MISSION</li><li>MEDIA</li><li>TEAM</li><li>LOCATIONS</li><li>SHOP</li><li>CONTACT</li><li class="login">LOGIN</li>
  </ul>
</nav>

<h1 class="abs center hero-title">WE LET YOUR EMPLOYEES<br>FROM HOME</h1>
<p class="abs hero-text">We develop an innovative VPN Appliance (Model-Name -&gt;Vale Nine) that gives small business the possibility literally setup the possibility for Companies to let their employees work from home.</p>
<div class="abs btn">LEARN MORE</div>

<!-- products -->
<div class="abs center eyebrow" style="top:718px">About our products</div>
<h2 class="abs center" style="top:736px;font-size:19px;font-weight:500;color:var(--ink)">*Vale Nine* products&nbsp; are rolled out in minutes.</h2>

<div class="abs card" style="left:175px;top:838px">
  <div class="card-art" role="img" aria-label="Illustration of a person connected to colleagues around a globe"></div>
  <h3>EMPLOYEES CAN CONNECT DIRECTLY</h3>
  <p>Lorem ipsum dolor sit amet, cons ectetur adipis csit amet, ur guvel faci lisis.</p>
</div>
<div class="abs card" style="left:475px;top:838px">
  <div class="card-art" role="img" aria-label="Illustration of a person working at a desk on a video call"></div>
  <h3>WORK FROM ANY LOCATION</h3>
  <p>Lorem ipsum dolor sit amet, cons ectetur adipis csit amet, ur guvel faci lisis.</p>
</div>
<div class="abs card" style="left:776px;top:838px">
  <div class="card-art" role="img" aria-label="Illustration of a person beside a laptop with a padlock and shield"></div>
  <h3>NO CHANGE THE COMPANY FIREWALL</h3>
  <p>Lorem ipsum dolor sit amet, cons ectetur adipis csit amet, ur guvel faci lisis.</p>
</div>

<!-- how it works -->
<svg class="abs" style="left:0;top:1271px" width="1200" height="820" aria-hidden="true">
  <path d="M0 10C120 0 230 170 300 330C350 450 520 540 440 660C380 760 150 800 0 810Z" fill="var(--sky)" opacity=".8"/>
  <path d="M760 0H1200V760C1100 720 1020 620 1010 500C1000 350 900 250 760 0Z" fill="#e9f0f9" opacity=".8"/>
</svg>
<div class="abs center eyebrow" style="top:1334px">Use case</div>
<h2 class="abs center section-title" style="top:1350px">How It Works</h2>
<div class="abs rule" style="top:1404px"></div>

<div class="abs dash" style="left:437px;top:1557px;width:60px"></div>
<div class="abs dash" style="left:702px;top:1557px;width:61px"></div>
<div class="abs dash" style="left:437px;top:1840px;width:60px"></div>

<div class="abs step" style="left:232px;top:1478px"><span class="num">1</span>
  <svg width="70" height="66" viewBox="0 0 70 66" fill="none" stroke="var(--blue)" stroke-width="2.5"><rect x="3" y="3" width="64" height="44" rx="3"/><rect x="12" y="11" width="40" height="26"/><path d="M20 20h20M20 27h12M28 47v10M42 47v10M18 60h34"/></svg>
  <h3>GO TO OUR PAGE</h3><p>Lorem ipsum dolor sit amet, consectetur adipiscing elit, ultrices gravida.</p></div>
<div class="abs step" style="left:497px;top:1478px"><span class="num">2</span>
  <svg width="70" height="64" viewBox="0 0 70 64" fill="none" stroke="var(--blue)" stroke-width="2.5"><path d="M4 18L28 6l24 12v28L28 58 4 46Z"/><path d="M4 18l24 12 24-12M28 30v28"/><rect x="44" y="30" width="22" height="30" rx="2"/><path d="M49 38h12M49 45h12M49 52h12"/></svg>
  <h3>SELECT PRODUCT</h3><p>Lorem ipsum dolor sit amet, consectetur adipiscing elit, ultrices gravida.</p></div>
<div class="abs step" style="left:763px;top:1478px"><span class="num">3</span>
  <svg width="70" height="70" viewBox="0 0 70 70" fill="none" stroke="var(--blue)" stroke-width="2.5"><rect x="8" y="3" width="38" height="54" rx="3"/><path d="M15 14l3 3 5-6M28 14h12M15 27l3 3 5-6M28 27h12M15 40l3 3 5-6M28 40h6"/><path d="M40 68V44a4 4 0 018 0v10l10 2v12"/></svg>
  <h3>SELECT PRODUCT</h3><p>Lorem ipsum dolor sit amet, consectetur adipiscing elit, ultrices gravida.</p></div>
<div class="abs step" style="left:232px;top:1760px"><span class="num">4</span>
  <svg width="56" height="62" viewBox="0 0 56 62" fill="none" stroke="var(--blue)" stroke-width="2.5"><rect x="3" y="3" width="50" height="56" rx="3"/><path d="M3 18h50M3 44h50"/><rect x="9" y="24" width="8" height="14"/><rect x="20" y="24" width="8" height="14"/><rect x="31" y="24" width="8" height="14"/><rect x="42" y="24" width="6" height="14"/><circle cx="12" cy="51" r="2"/><circle cx="44" cy="51" r="2"/></svg>
  <h3>CONNECT TO ANY SWITCH</h3><p>Lorem ipsum dolor sit amet, consectetur adipiscing elit, ultrices gravida.</p></div>
<div class="abs step" style="left:497px;top:1760px;width:199px"><span class="num">5</span>
  <svg width="72" height="68" viewBox="0 0 72 68" fill="none" stroke="var(--blue)" stroke-width="2.5"><rect x="26" y="3" width="42" height="34" rx="2"/><circle cx="47" cy="20" r="7"/><path d="M47 37v8M38 45h18"/><circle cx="14" cy="46" r="10"/><circle cx="14" cy="46" r="3"/><path d="M4 62h30"/><circle cx="60" cy="58" r="6"/></svg>
  <h3>INSTALL SOFTWARE</h3><p>Lorem ipsum dolor sit amet, consectetur adipiscing elit, ultrices gravida.</p></div>

<!-- testimonials -->
<svg class="abs" style="left:870px;top:2070px" width="330" height="630" aria-hidden="true">
  <path d="M330 0C230 50 150 160 160 260C170 350 220 400 150 480C100 540 30 560 0 630H330Z" fill="var(--sky)" opacity=".9"/>
</svg>
<div class="abs center eyebrow" style="top:2136px">What customers are saying</div>
<h2 class="abs center section-title" style="top:2152px">Testimonials</h2>
<div class="abs rule" style="top:2200px"></div>
<div class="abs center" style="top:2268px;color:var(--accent);font-size:11px;letter-spacing:1px">★★★★★</div>
<div class="abs" role="img" aria-label="Customer portrait" style="left:561px;top:2294px;width:78px;height:78px;border-radius:50%;background:linear-gradient(150deg,#c9a27e,#7a6a5e);border:3px solid #e4ebf5;box-shadow:0 4px 10px rgba(0,0,0,.2)"></div>
<p class="abs quote">Lorem ipsum dolor sit amet, consectetur adipiscing elit, sed do eiusmod tempor incididunt ut labore et dolore magna aliquapiscing elit, sed do eiusmod tempor incididunt ut labore et dolore magna aliqua.</p>
<svg class="abs arrow" style="left:210px" width="24" height="36" viewBox="0 0 24 36"><path d="M18 4L6 18l12 14" fill="none" stroke="var(--blue)" stroke-width="4"/></svg>
<svg class="abs arrow" style="left:963px" width="24" height="36" viewBox="0 0 24 36"><path d="M6 4l12 14L6 32" fill="none" stroke="var(--blue)" stroke-width="4"/></svg>
<div class="abs center" style="top:2515px;font-size:11.5px;font-weight:500">MAREN OAKLEY</div>
<div class="abs center" style="top:2537px;font-size:10.5px;color:var(--muted)">Founder of&nbsp; her Company</div>
<svg class="abs" style="left:582px;top:2577px" width="40" height="14" aria-hidden="true"><circle cx="8" cy="7" r="5" fill="none" stroke="var(--blue)" stroke-width="1.5"/><circle cx="8" cy="7" r="3" fill="var(--blue)"/><circle cx="28" cy="7" r="3.5" fill="var(--blue)"/></svg>

<!-- partners -->
<div class="abs center eyebrow" style="top:2680px">We have a successful history</div>
<h2 class="abs center section-title" style="top:2697px">Our partners</h2>
<div class="abs rule" style="top:2744px"></div>
<div class="abs partners">
  <div class="badge"></div><div class="badge"></div><div class="badge"></div><div class="badge"></div><div class="badge"></div>
</div>

<!-- footer -->
<svg class="abs footer-bg" viewBox="0 0 1200 483" aria-hidden="true">
  <path d="M0 150C60 80 180 20 300 15C420 10 480 70 620 120C760 170 850 160 960 110C1050 70 1130 30 1200 40V483H0Z" fill="var(--deep)"/>
  <path d="M0 442H1200" stroke="#3a5a92" stroke-width="1"/>
</svg>

<div class="abs foot" style="left:232px;top:3082px;width:240px">
  <div style="display:flex;align-items:center;gap:8px;font-size:25px;font-weight:500;color:#2b4f8c"><span style="width:24px;height:24px;background:var(--bright);border-radius:3px"></span>CopperVale</div>
  <div class="foot-rule" style="margin-top:12px"></div>
  <p style="margin-top:26px">Lorem ipsum dolor sit amet, consectetur adipiscing elit, sed do eiusmod tempor incididunt ut labore et dolore magna aliqua. Ut enim ad minim veniam, quis nostrud.</p>
  <p style="margin-top:10px">Qcididunt ut labore et dolore magna aliqua. Ut enim ad minim veniam, quis nostrud.</p>
  <div style="display:flex;gap:12px;margin-top:16px"><span class="social"></span><span class="social"></span><span class="social"></span></div>
</div>

<div class="abs foot" style="left:599px;top:3097px">
  <h4>QUICK LINKS</h4>
  <div class="foot-rule" style="width:78px;margin-bottom:32px"></div>
  <ul class="foot-links"><li>Home</li><li>Blog</li><li>About Us</li><li>Contact Us</li><li>News</li><li>Insurance Plan</li><li>Sitemap</li></ul>
</div>

<div class="abs foot" style="left:813px;top:3097px;width:200px">
  <h4>LET'S CONNECT</h4>
  <div class="foot-rule" style="width:85px;margin-bottom:26px"></div>
  <div class="contact-row"><svg width="20" height="20" viewBox="0 0 24 24"><path d="M6.6 10.8a15 15 0 006.6 6.6l2.2-2.2a1 1 0 011-.25 11 11 0 003.6.6 1 1 0 011 1V20a1 1 0 01-1 1A17 17 0 013 4a1 1 0 011-1h3.5a1 1 0 011 1 11 11 0 00.6 3.6 1 1 0 01-.25 1z" fill="#3d8df5"/></svg><span>55 010 2468</span></div>
  <div class="contact-row" style="margin-top:14px"><svg width="20" height="22" viewBox="0 0 24 24"><path d="M12 2a7 7 0 00-7 7c0 5 7 13 7 13s7-8 7-13a7 7 0 00-7-7zm0 9.5A2.5 2.5 0 1112 6.5a2.5 2.5 0 010 5z" fill="#3d8df5"/></svg><span>Harbour Lane<br>Eastport 4100</span></div>
  <div class="contact-row" style="margin-top:14px"><svg width="20" height="20" viewBox="0 0 24 24"><path d="M2 11l20-8-6 18-5-7z" fill="#3d8df5"/></svg><span>hello@coppervale.example</span></div>
</div>

<div class="abs center" style="top:3364px;color:var(--white);font-size:10.5px">© 2022 CopperVale LLC.</div>

</body>
</html>
```